Start up in business consultancy needs a business card

We need the business card's layout (we have already the logo). Our business is concerned on consultancy services delivered to companies on the matter of sustainability. Business card should be enough essentials and professional style.

Side A with the following info:
logo + a space for the claim (still to identify) + website of the company

Side B with the following info:
Name of business card holder + title of the business card holder + address of the company + space for mobile number, phone number, fax number + e-mail of business card holder + graphic details around.

Target Market(s)

Business of any sector

Industry/Entity Type

Business Service

Contact Information for Business Card

Name of the company:
Lumeroca srl
Società Benefit

Address of the company:
Via Pescoli, 7
21099 - Gallarate (VA)

Website:
www.lumeroca-esempio.it

Name of the BC' holder:
Ettore Valsenzi

Title:
Co-fondatore

Email:
ettore@lumeroca-esempio.it

Mobile:
+39 351 602 7415
Phone:
+39 351 602 7415
Fax:
+39 351 602 7415

Font styles to use
Other font styles liked:
• new gothic

```html
<!DOCTYPE html>
<html lang="it">
<head>
<meta charset="utf-8">
<title>Lumeroca – biglietto da visita</title>
<link rel="stylesheet" href="https://fonts.googleapis.com/css2?family=Oswald:wght@500;600&family=Arimo:wght@400&display=swap">
<style>
  :root {
    --brand-blue: #1f68b4;
    --faint-blue: #e3edf7;
    --ink: #2b2b2b;
    --ink-soft: #444;
    --paper: #ffffff;
    --backdrop: #e9eaec;
    --dark-block: #151515;
  }
  * { box-sizing: border-box; margin: 0; padding: 0; }
  html, body { width: 1200px; height: 900px; overflow: hidden; }
  body {
    background: var(--backdrop);
    font-family: "Arimo", Arial, sans-serif;
    position: relative;
  }
  .card {
    position: absolute;
    left: 280px;
    width: 640px;
    height: 390px;
    background: var(--paper);
    overflow: hidden;
    box-shadow: 0 6px 18px rgba(0,0,0,0.18);
  }
  .card--front { top: 30px; }
  .card--back { top: 480px; }
  .card__deco { position: absolute; inset: 0; }

  /* Front */
  .brand {
    position: absolute;
    left: 110px;
    top: 52px;
    display: flex;
    align-items: center;
    gap: 14px;
  }
  .brand__mark {
    width: 70px; height: 70px;
    border: 4px solid var(--brand-blue);
    border-radius: 50%;
  }
  .brand__name {
    font-family: "Arimo", Arial, sans-serif;
    font-size: 44px;
    color: var(--brand-blue);
    letter-spacing: 0.5px;
  }
  .brand__tagline {
    position: absolute;
    left: 210px;
    top: 140px;
    font-family: "Oswald", "Arial Narrow", sans-serif;
    font-weight: 600;
    font-size: 17px;
    color: var(--brand-blue);
    letter-spacing: 0.3px;
  }
  .claim-line {
    position: absolute;
    height: 0;
    border-top: 2px dotted var(--ink);
  }
  .claim-line--one { left: 210px; right: 50px; top: 210px; }
  .claim-line--two { left: 70px; right: 50px; top: 262px; }
  .website {
    position: absolute;
    left: 0; right: 0;
    top: 330px;
    text-align: center;
    font-size: 16px;
    color: var(--ink-soft);
  }
  .website__name { color: var(--brand-blue); }
  .edge-tab {
    position: absolute;
    width: 32px; height: 9px;
    background: var(--brand-blue);
  }
  .edge-tab--right { right: 0; top: 120px; }
  .edge-tab--left { left: 0; top: 360px; }

  /* Back */
  .side-block {
    position: absolute;
    left: 0; top: 172px;
    width: 26px; height: 30px;
    background: var(--dark-block);
  }
  .side-bar {
    position: absolute;
    left: 26px; top: 202px;
    width: 7px; bottom: 0;
    background: var(--brand-blue);
  }
  .holder {
    position: absolute;
    left: 62px;
    top: 150px;
  }
  .holder__name {
    font-family: "Oswald", "Arial Narrow", sans-serif;
    font-weight: 600;
    font-size: 22px;
    color: var(--brand-blue);
    text-transform: uppercase;
    line-height: 1.1;
  }
  .holder__title {
    font-size: 16px;
    color: var(--ink);
    margin-top: 2px;
  }
  .holder__address {
    margin-top: 16px;
    font-size: 16px;
    line-height: 1.3;
    color: var(--brand-blue);
  }
  .contacts {
    list-style: none;
    margin-top: 14px;
  }
  .contacts__item {
    display: flex;
    align-items: center;
    gap: 12px;
    font-size: 17px;
    line-height: 1.45;
    color: var(--brand-blue);
  }
  .contacts__icon { width: 14px; height: 14px; flex: none; }
</style>
</head>
<body>

<section class="card card--front" aria-label="Fronte del biglietto">
  <svg class="card__deco" width="640" height="390" aria-hidden="true">
    <circle cx="70" cy="300" r="155" fill="none" stroke="var(--faint-blue)" stroke-width="12"/>
  </svg>
  <div class="brand">
    <span class="brand__mark"></span>
    <span class="brand__name">lumeroca</span>
  </div>
  <p class="brand__tagline">SOCIETÀ BENEFIT</p>
  <span class="claim-line claim-line--one"></span>
  <span class="claim-line claim-line--two"></span>
  <p class="website">www.<span class="website__name">lumeroca-esempio</span>.it</p>
  <span class="edge-tab edge-tab--right"></span>
  <span class="edge-tab edge-tab--left"></span>
</section>

<section class="card card--back" aria-label="Retro del biglietto">
  <svg class="card__deco" width="640" height="390" aria-hidden="true">
    <circle cx="560" cy="110" r="160" fill="none" stroke="var(--faint-blue)" stroke-width="12"/>
  </svg>
  <span class="side-block"></span>
  <span class="side-bar"></span>
  <div class="holder">
    <p class="holder__name">Ettore Valsenzi</p>
    <p class="holder__title">Co-fondatore</p>
    <p class="holder__address">Via Pescoli, 7<br>21099 - Castelmora (CM)</p>
    <ul class="contacts">
      <li class="contacts__item">
        <svg class="contacts__icon" viewBox="0 0 14 14" aria-label="Cellulare"><rect x="3.5" y="0.8" width="7" height="12.4" rx="1.2" fill="none" stroke="var(--ink)" stroke-width="1.4"/><circle cx="7" cy="11" r="0.8" fill="var(--ink)"/></svg>
        +39 351 602 7415
      </li>
      <li class="contacts__item">
        <svg class="contacts__icon" viewBox="0 0 14 14" aria-label="Telefono"><path d="M3 1 L5.2 3.4 L4 5 C5 7.2 6.8 9 9 10 L10.6 8.8 L13 11 L11.6 13 C6 12.5 1.5 8 1 2.4 Z" fill="var(--ink)"/></svg>
        +39 351 602 7415
      </li>
      <li class="contacts__item">
        <svg class="contacts__icon" viewBox="0 0 14 14" aria-label="Fax"><rect x="3.5" y="1" width="7" height="4" fill="var(--ink)"/><rect x="1" y="5.5" width="12" height="6" rx="1" fill="var(--ink)"/><rect x="3.5" y="10" width="7" height="3" fill="var(--ink)"/></svg>
        +39 351 602 7415
      </li>
      <li class="contacts__item">
        <svg class="contacts__icon" viewBox="0 0 14 14" aria-label="E-mail"><rect x="1" y="3" width="12" height="8.5" fill="none" stroke="var(--ink)" stroke-width="1.3"/><path d="M1 3 L7 8 L13 3" fill="none" stroke="var(--ink)" stroke-width="1.3"/></svg>
        ettore@lumeroca-esempio.it
      </li>
    </ul>
  </div>
</section>

</body>
</html>
```